Update cover page from corporate ppt template

We would like you to design a new cover page for our corporate presentation template

Attached you will find our existing template with the previous cover pages used in the past years.

As you can see, we have used transparency lines in different directions and also tried to develop a new design with mosaic/squares but we are not entirely satisfied (logo lost in the sky, ...)

You can reuse the same picture (mountain with the bridge, i.e not the one of the last cover page)

Feel free to come up with new ideas

```html
<!DOCTYPE html>
<html lang="en">
<head>
<meta charset="utf-8">
<title>Board of Directors – Cover Options</title>
<link rel="stylesheet" href="https://fonts.googleapis.com/css2?family=Montserrat:wght@400;500&family=Marcellus&display=swap">
<style>
  :root {
    --page: #ffffff;
    --navy: #1a2041;
    --periwinkle: #7b90c8;
    --periwinkle-soft: #c3cfea;
    --sand: #ddd2bf;
    --tan: #c2a97f;
    --ink: #141414;
    --date: #c4a57c;
    --date-on-navy: #d8c29b;
    --wordmark-light: #6d6d72;
    --wordmark-dark: #8a93ad;
    --photo-top: #8fbfe0;
    --photo-bottom: #4a7398;
  }
  * { margin: 0; padding: 0; box-sizing: border-box; }
  html, body { width: 1200px; height: 2194px; overflow: hidden; background: var(--page); }
  .sheet { position: relative; width: 1200px; height: 2194px; }
  .slide {
    position: absolute; width: 450px; height: 337px; overflow: hidden;
    box-shadow: 8px 10px 22px rgba(0,0,0,0.28);
    background: var(--page);
  }
  .slide--navy { background: var(--navy); }
  .slide-art { position: absolute; inset: 0; width: 100%; height: 100%; display: block; }
  .slide-title {
    position: absolute; left: var(--tx); top: var(--ty);
    font-family: "Montserrat", sans-serif; color: var(--ink);
  }
  .wordmark {
    font-family: "Marcellus", serif; font-size: 29px; letter-spacing: 1px;
    color: var(--wordmark-light); line-height: 1; margin-bottom: 14px;
  }
  .slide-heading { font-size: 26px; font-weight: 400; line-height: 1.12; }
  .slide-date { font-size: 16px; color: var(--date); margin-top: 10px; }
  .slide--navy .slide-heading { color: #ffffff; }
  .slide--navy .wordmark { color: var(--wordmark-dark); }
  .slide--navy .slide-date { color: var(--date-on-navy); }
  .col-a { left: 92px; } .col-b { left: 653px; }
  .row-1 { top: 157px; } .row-2 { top: 541px; } .row-3 { top: 925px; }
  .row-4 { top: 1309px; } .row-5 { top: 1694px; }
  .gradients { position: absolute; width: 0; height: 0; }
</style>
</head>
<body>
<svg class="gradients" aria-hidden="true">
  <defs>
    <linearGradient id="photo-fill" gradientUnits="userSpaceOnUse" x1="0" y1="0" x2="0" y2="397">
      <stop offset="0" stop-color="var(--photo-top)"/>
      <stop offset="1" stop-color="var(--photo-bottom)"/>
    </linearGradient>
  </defs>
</svg>

<main class="sheet">
  <!-- Row 1 -->
  <section class="slide col-a row-1">
    <svg class="slide-art" viewBox="0 0 530 397" preserveAspectRatio="none">
      <path d="M305,0 Q392,198 300,397 H530 V0Z" fill="var(--periwinkle)"/>
      <path d="M322,0 Q409,198 317,397 H530 V0Z" fill="var(--sand)"/>
      <path role="img" aria-label="Photo of a snow-capped mountain peak reflected in an alpine lake" d="M335,0 Q422,198 330,397 H530 V0Z" fill="url(#photo-fill)"/>
    </svg>
    <div class="slide-title" style="--tx:36px;--ty:89px">
      <div class="wordmark">NORVAL</div>
      <h1 class="slide-heading">Board of<br>Directors</h1>
      <p class="slide-date">May 2024</p>
    </div>
  </section>

  <section class="slide slide--navy col-b row-1">
    <svg class="slide-art" viewBox="0 0 530 397" preserveAspectRatio="none">
      <path d="M195,0 Q282,198 190,397 H530 V0Z" fill="var(--periwinkle)"/>
      <path d="M212,0 Q299,198 207,397 H530 V0Z" fill="var(--sand)"/>
      <path role="img" aria-label="Photo of a snow-capped mountain peak reflected in an alpine lake" d="M225,0 Q312,198 220,397 H530 V0Z" fill="url(#photo-fill)"/>
    </svg>
    <div class="slide-title" style="--tx:36px;--ty:89px">
      <div class="wordmark">NORVAL</div>
      <h1 class="slide-heading">Board of<br>Directors</h1>
      <p class="slide-date">May 2024</p>
    </div>
  </section>

  <!-- Row 2 -->
  <section class="slide col-a row-2">
    <svg class="slide-art" viewBox="0 0 530 397" preserveAspectRatio="none">
      <path d="M270,0 Q195,198 275,397 H530 V0Z" fill="var(--periwinkle)"/>
      <path d="M285,0 Q210,198 290,397 H530 V0Z" fill="var(--sand)"/>
      <path role="img" aria-label="Photo of a snow-capped mountain peak reflected in an alpine lake" d="M300,0 Q225,198 305,397 H530 V0Z" fill="url(#photo-fill)"/>
    </svg>
    <div class="slide-title" style="--tx:36px;--ty:89px">
      <div class="wordmark">NORVAL</div>
      <h1 class="slide-heading">Board of<br>Directors</h1>
      <p class="slide-date">May 2024</p>
    </div>
  </section>

  <section class="slide slide--navy col-b row-2">
    <svg class="slide-art" viewBox="0 0 530 397" preserveAspectRatio="none">
      <path d="M235,0 Q155,198 255,397 H530 V0Z" fill="var(--sand)"/>
      <path d="M250,0 Q170,198 270,397 H530 V0Z" fill="var(--periwinkle)"/>
      <path role="img" aria-label="Photo of a snow-capped mountain peak reflected in an alpine lake" d="M265,0 Q185,198 285,397 H530 V0Z" fill="url(#photo-fill)"/>
    </svg>
    <div class="slide-title" style="--tx:36px;--ty:89px">
      <div class="wordmark">NORVAL</div>
      <h1 class="slide-heading">Board of<br>Directors</h1>
      <p class="slide-date">May 2024</p>
    </div>
  </section>

  <!-- Row 3 -->
  <section class="slide slide--navy col-a row-3">
    <svg class="slide-art" viewBox="0 0 530 397" preserveAspectRatio="none">
      <path d="M262,0 Q180,198 265,397 H530 V0Z" fill="var(--periwinkle)"/>
      <path d="M277,0 Q195,198 280,397 H530 V0Z" fill="var(--tan)"/>
      <path role="img" aria-label="Photo of a snow-capped mountain peak reflected in an alpine lake" d="M297,0 Q215,198 300,397 H530 V0Z" fill="url(#photo-fill)"/>
    </svg>
    <div class="slide-title" style="--tx:36px;--ty:89px">
      <div class="wordmark">NORVAL</div>
      <h1 class="slide-heading">Board of<br>Directors</h1>
      <p class="slide-date">May 2024</p>
    </div>
  </section>

  <section class="slide col-b row-3">
    <svg class="slide-art" viewBox="0 0 530 397" preserveAspectRatio="none">
      <rect role="img" aria-label="Photo of a snow-capped mountain peak reflected in an alpine lake" width="530" height="397" fill="url(#photo-fill)"/>
      <path d="M0,0 H440 Q340,150 190,195 Q100,125 0,100Z" fill="var(--navy)" opacity="0.72"/>
      <path d="M0,100 Q300,140 440,397 H0Z" fill="#ffffff"/>
    </svg>
    <div class="slide-title" style="--tx:48px;--ty:168px">
      <div class="wordmark">NORVAL</div>
      <h1 class="slide-heading">Board of<br>Directors</h1>
      <p class="slide-date">May 2024</p>
    </div>
  </section>

  <!-- Row 4 -->
  <section class="slide col-a row-4">
    <svg class="slide-art" viewBox="0 0 530 397" preserveAspectRatio="none">
      <rect role="img" aria-label="Photo of a snow-capped mountain peak reflected in an alpine lake" width="530" height="397" fill="url(#photo-fill)"/>
      <path d="M0,0 H440 Q340,150 190,195 Q100,125 0,100Z" fill="var(--tan)" opacity="0.78"/>
      <path d="M0,100 Q300,140 440,397 H0Z" fill="#ffffff"/>
    </svg>
    <div class="slide-title" style="--tx:48px;--ty:166px">
      <div class="wordmark">NORVAL</div>
      <h1 class="slide-heading">Board of<br>Directors</h1>
      <p class="slide-date">May 2024</p>
    </div>
  </section>

  <section class="slide col-b row-4">
    <svg class="slide-art" viewBox="0 0 530 397" preserveAspectRatio="none">
      <rect role="img" aria-label="Photo of a snow-capped mountain peak reflected in an alpine lake" width="530" height="397" fill="url(#photo-fill)"/>
      <circle cx="110" cy="40" r="290" fill="var(--periwinkle-soft)" opacity="0.85"/>
      <circle cx="110" cy="40" r="268" fill="var(--periwinkle)"/>
      <circle cx="110" cy="40" r="255" fill="#ffffff"/>
      <path d="M0,0H530V397H0Z M580,40 A470,470 0 1,0 -360,40 A470,470 0 1,0 580,40Z" fill="#ffffff" fill-rule="evenodd"/>
    </svg>
    <div class="slide-title" style="--tx:44px;--ty:75px">
      <div class="wordmark">NORVAL</div>
      <h1 class="slide-heading">Board of<br>Directors</h1>
      <p class="slide-date">May 2024</p>
    </div>
  </section>

  <!-- Row 5 -->
  <section class="slide col-a row-5">
    <svg class="slide-art" viewBox="0 0 530 397" preserveAspectRatio="none">
      <rect role="img" aria-label="Photo of a snow-capped mountain peak reflected in an alpine lake" width="530" height="397" fill="url(#photo-fill)"/>
      <circle cx="110" cy="40" r="290" fill="var(--periwinkle-soft)" opacity="0.85"/>
      <circle cx="110" cy="40" r="268" fill="var(--periwinkle)"/>
      <circle cx="110" cy="40" r="255" fill="#ffffff"/>
      <path d="M0,0H530V397H0Z M580,40 A470,470 0 1,0 -360,40 A470,470 0 1,0 580,40Z" fill="var(--navy)" fill-rule="evenodd"/>
    </svg>
    <div class="slide-title" style="--tx:44px;--ty:75px">
      <div class="wordmark">NORVAL</div>
      <h1 class="slide-heading">Board of<br>Directors</h1>
      <p class="slide-date">May 2024</p>
    </div>
  </section>

  <section class="slide slide--navy col-b row-5">
    <svg class="slide-art" viewBox="0 0 530 397" preserveAspectRatio="none">
      <rect role="img" aria-label="Photo of a snow-capped mountain peak reflected in an alpine lake" width="530" height="397" fill="url(#photo-fill)"/>
      <circle cx="110" cy="40" r="290" fill="var(--periwinkle-soft)" opacity="0.85"/>
      <circle cx="110" cy="40" r="268" fill="var(--periwinkle)"/>
      <circle cx="110" cy="40" r="255" fill="var(--navy)"/>
      <path d="M0,0H530V397H0Z M580,40 A470,470 0 1,0 -360,40 A470,470 0 1,0 580,40Z" fill="var(--tan)" fill-rule="evenodd"/>
    </svg>
    <div class="slide-title" style="--tx:44px;--ty:75px">
      <div class="wordmark">NORVAL</div>
      <h1 class="slide-heading">Board of<br>Directors</h1>
      <p class="slide-date">May 2024</p>
    </div>
  </section>
</main>
</body>
</html>
```